Watch brand needs new business cards

Kestrel Timepiece Company are looking for a new business card design incorporating our logo and brand colours as per our website.

Design should be 90x55mm with 3mm print margin from edges and 3mm external bleed.

Card should be double sided, e.g. logo one side, personal details on the other.

Logo will be provided as a vector.

The card must be able to show:
- Staff name
- Position
- Office Address
- Email
- Telephone number
- Website address

Final work must be provided in an editable format to allow us to add staff details (e.g. an AI or PSD file).

```html
<!DOCTYPE html>
<html lang="en">
<head>
<meta charset="utf-8">
<title>Kestrel Timepiece Company – Business Cards</title>
<link rel="stylesheet" href="https://fonts.googleapis.com/css2?family=Cinzel:wght@600&family=Open+Sans:wght@400;600&display=swap">
<style>
  :root {
    --backdrop: #6e6e6e;
    --card-dark: #050505;
    --card-mid: #1c1c1c;
    --ink: #ffffff;
    --ink-soft: #e6e6e6;
    --rule: #d9d9d9;
  }
  * { margin: 0; padding: 0; box-sizing: border-box; }
  html, body {
    width: 1200px; height: 1000px; overflow: hidden;
    background: var(--backdrop);
  }
  .canvas { position: relative; width: 1200px; height: 1000px; }
  .card {
    position: absolute; left: 220px; width: 760px; height: 434px;
    background: linear-gradient(125deg, var(--card-dark) 0%, var(--card-dark) 52%, var(--card-mid) 58%, #0c0c0c 100%);
    box-shadow: 0 4px 14px rgba(0,0,0,.45);
    color: var(--ink);
  }
  .card--front { top: 50px; }
  .card--back { top: 524px; }

  .brand { position: absolute; text-align: center; font-family: "Cinzel", serif; font-weight: 600; color: var(--ink); }
  .brand__mark { display: block; margin: 0 auto; border: 4px solid var(--ink); border-radius: 50%; }
  .brand__name { display: block; line-height: 1; }
  .brand__sub { display: block; line-height: 1; }

  .card--front .brand { left: 0; width: 760px; top: 110px; }
  .card--front .brand__mark { width: 124px; height: 124px; }
  .card--front .brand__name { font-size: 62px; margin-top: 64px; letter-spacing: 1px; }
  .card--front .brand__sub { font-size: 19px; letter-spacing: 3.5px; margin-top: 8px; }

  .card--back .brand { left: 38px; width: 380px; top: 130px; }
  .card--back .brand__mark { width: 92px; height: 92px; border-width: 3px; }
  .card--back .brand__name { font-size: 46px; margin-top: 50px; letter-spacing: 1px; }
  .card--back .brand__sub { font-size: 15px; letter-spacing: 3px; margin-top: 6px; }

  .divider { position: absolute; left: 438px; top: 130px; width: 2px; height: 172px; background: var(--rule); }

  .contact { position: absolute; left: 462px; top: 128px; font-family: "Open Sans", sans-serif; color: var(--ink-soft); font-size: 15.5px; line-height: 22px; }
  .contact__name { font-weight: 600; font-size: 19px; color: var(--ink); line-height: 24px; }
  .contact__role { margin-bottom: 11px; }
  .contact__address { margin-bottom: 11px; }
  .contact__line { display: flex; align-items: center; gap: 5px; }
  .contact__line svg { width: 12px; height: 12px; flex: none; fill: var(--ink-soft); }
</style>
</head>
<body>
<main class="canvas">
  <section class="card card--front" aria-label="Card front">
    <div class="brand">
      <span class="brand__mark"></span>
      <span class="brand__name">KESTREL</span>
      <span class="brand__sub">TIMEPIECE COMPANY</span>
    </div>
  </section>

  <section class="card card--back" aria-label="Card back">
    <div class="brand">
      <span class="brand__mark"></span>
      <span class="brand__name">KESTREL</span>
      <span class="brand__sub">TIMEPIECE COMPANY</span>
    </div>
    <div class="divider"></div>
    <div class="contact">
      <div class="contact__name">Daniel Hart</div>
      <div class="contact__role">Founder &amp; CEO</div>
      <div class="contact__address">Street name, Suite 100<br>State, Zip Code, Country</div>
      <div class="contact__line">
        <svg viewBox="0 0 12 12"><path d="M2.5 0.5l2 2.5-1.2 1.3c.7 1.6 1.8 2.7 3.4 3.4L8 6.5l2.5 2-1.3 2.5C4.5 10.5 1.5 7.5 0.5 2z"/></svg>
        <span>012-345-6789</span>
      </div>
      <div class="contact__line">
        <svg viewBox="0 0 12 12"><path d="M0.5 2.5h11v7h-11z M1 3l5 3.5L11 3" stroke="#050505" stroke-width=".9"/></svg>
        <span>info@youremail.com</span>
      </div>
      <div class="contact__line">
        <svg viewBox="0 0 12 12"><circle cx="6" cy="6" r="5.5"/><path d="M0.5 6h11M6 0.5v11M6 0.5c-3 3-3 8 0 11M6 0.5c3 3 3 8 0 11" stroke="#050505" stroke-width=".8" fill="none"/></svg>
        <span>www.yourwebsite.com</span>
      </div>
    </div>
  </section>
</main>
</body>
</html>
```